Creating business cards for our new private medical clinic in London

Hey everyone,

We are starting a new private medical clinic in central London. We already have our logo (please see the 2 different layouts of the logo attached.) Please note that we are not restricted to using only this font in the card though.

The cards will be printed by "Pekko." The cards have a textured surface and a coloured middle layer - please see this webpage for the exact product spec (https://www.pekkoprint.example/uk/products/velvet/business-cards.html). We're overall looking for a modern yet highly professional look. We'd like the cards to have Square edges and NOT rounded please.

We need a standard card that uses one or both of our logo's colours (blue and green), and another card for premium customers, that uses black with either gold/silver/bronze. On the black coloured cads, please could you add the word "Black Account" or the word "Black" under the logo text - wherever you think it looks best?

_________________

AMENDMENT TO BRIEF:

1) The first batch of our cards are to be promotional cards and need to have more information. Could please have one card that is more like an "information card" that has the following information: - (There's a lot there and we might need to slim this down once we see the cards.)

GP appointments £70
-Feeling unwell
-Referrals to private specialists
-Sexual health check up
-Contraception
-Second opinion

Launch Offer
First appointment £40 with this card until 30 September 2017

Book online

2) Could you see whether we could add a 'strap line' to the card, something like: “Stay in Optimal Health”

_____________

The files attached have 2 versions of our logo - one linear and with the words 'stacked'; we think that the stacked logo may work better for the business card but we'd love to see different versions.

On one side of the card could we please see a coloured background, with a design containing our logo? On the other side of the card, please could we have a different coloured or white background and the information below.

Address: THE HARROWFIELD CLINIC @ FitVanta, 19 Bramblecote Lane, London, EC2Z 4QJ
Open: Mon-Fri (early & late appointments)
Book Online: www.harrowfieldclinic.example
Email: bookings@harrowfieldclinic.example
Phone number: (We don't have this yet - but please leave a space for this to go into.)

Other possible design features:

Because our clinic is located in the financial district of London, anything that represents this (e.g. The City of London's skyline - i.e. financial district - could look nice (example buildings include: The Pinecone, The Teacup-Tower, The Wedgehouse, St Aldric Minster, Keep of Brennmoor, Gantry Crossing, The Spindle). We wondered whether a outline or drawing of these buildings in the background of the card could look nice. Please see the image link below to get an idea of the skyline we're looking for:

https://img.stockvale.example/z/skyline-hand-drawn-city-pastel-shades-heritage-buildings-futuristic-81920457.jpg

The following image links are examples of cards that we've seen online and like the overall feel of (of course our colours are different):

http://www.craftnook.example/diverse/2/goodcards/73014589122.jpg
http://cardheron.example/wp-content/uploads/2013/01/cool-business-cards-saffron.jpg
https://cardfolio.example/wp-content/uploads/20461-cool-business-card-mockup.jpg
http://www.plinthworks.example/wp-content/uploads/edd/2015/08/Modern-Tutor-Business-Card-Template-Preview.jpg
http://lorvelandkit.example/wp-content/uploads/2017/01/design-a-business-card-cool-business-card-designsqx83.jpg
http://makerspindle.example/resources/files/articles/harbor-print/copper-foil-business-cards.jpg

STATIONARY:
We will also need the following stationary designed by our chosen designer. We’d like stationary to use one or both the colours of our logo (ie Green and Blue). Please use these colours to add any additional design features to stationary - other similar palette colours can also be used. Our logo font is - abeatbyKai - and this could be used in other parts of the stationary, but please feel free to try other fonts too. We prefer sans serif fonts.

Overall - we are open to all ideas but we need a look and feel that looks modern and highly professional. For our letter, prescription and medical report templates we need these to be PDFs and word processing files that can merge relevant data and text into different sections.

The information required on various pieces of stationary are as follows:

Letterheads:
These need to have:
Clinic's: Logo / Address / Phone Number / Website / Email address / Recipients address.
The letter can have address data either at the top or as a footer. We're happy to see designs that use either to see which one looks best (same goes for other pieces of stationary too.)

Invoices:
Invoice number: (Unique code for document)
Invoice Date:
Clinic’s: Logo / Address / Phone Number / Website / Email address
Services: Service Code / Name of Service / Price
Total Price:
PAYLO, Cardwise and Northern Remit Logos
Patient details: Patient’s Name / Address

Prescription Pads:
Prescription number: (Unique code for document)
Clinic details: Clinic’s Logo / Address / Phone Number / Website / Email address
Patient details needed include: Patient’s Name / Date of birth / address
Blank space required to write the name of medication
Doctors Signature: and space for signature
MPB Number: and space for this to be entered

Templates for our medical reports:
These are reports we will be printed (on good quality paper) for patients after they have had a complete health check. They will include a text summary, and the results of any tests (with graphs) and images of scans. Please could we see how text/titles/headings/tables etc could be styled?
They will need the following details: -
Clinic details needed include: Clinic’s Logo / Address / Phone Number / Website / Email address
Date of Report:
Then the following sections need to be includes:
1) Free Text Space
2) Space for images and text
3) Space for blood test and text

___________________

Thanks so much everyone.

All the best,

Tev and Dane

Target Market(s)

City of London
Private Healthcare

Industry/Entity Type

Health Care

Contact Information for Business Card

Font styles to use
Sans Serif

Colors
33a6d7
25a0d3
add136
9bcb3c
cadf82
85acd3
3276b5
0255a3
85cae6

Requirements
Must have
• Please see project description for details.
Nice to have
• Perhaps a outline/drawing/illustration of the City of London skyline (i.e. the Pinecone and surrounding buildings)

```html
<!DOCTYPE html>
<html lang="en">
<head>
<meta charset="utf-8">
<title>The Harrowfield Clinic – Business Cards</title>
<link rel="stylesheet" href="https://fonts.googleapis.com/css2?family=Open+Sans:wght@400;600;700&family=Quicksand:wght@400&display=swap">
<style>
  :root {
    --page-bg: #8e8e8e;
    --card-white: #fbfbf9;
    --brand-blue: #33a6d7;
    --brand-blue-deep: #25a0d3;
    --brand-green: #9bcb3c;
    --brand-green-bright: #add136;
    --brand-green-pale: #cadf82;
    --text-grey: #4a4a4a;
    --on-green: #ffffff;
  }
  * { box-sizing: border-box; margin: 0; padding: 0; }
  html, body {
    width: 1101px; height: 1200px; overflow: hidden;
    background: var(--page-bg);
    font-family: "Open Sans", Arial, sans-serif;
  }
  .canvas { position: relative; width: 1101px; height: 1200px; }
  .card {
    position: absolute; left: 130px; width: 840px; height: 460px;
    overflow: hidden;
  }
  .card--contact { top: 90px; background: var(--card-white); }
  .card--brand { top: 650px; background: var(--brand-green); }

  /* Name block: wordmark with the tagline set flush right beneath it */
  .brand-name {
    display: inline-flex; flex-direction: column; align-items: flex-end;
  }
  .wordmark {
    font-family: "Quicksand", "Trebuchet MS", sans-serif;
    font-weight: 400; line-height: 1; white-space: nowrap;
  }
  .tagline {
    font-family: "Open Sans", Arial, sans-serif;
    font-weight: 600; letter-spacing: 2.5px; text-transform: uppercase;
    white-space: nowrap; margin-top: 8px;
  }

  /* Contact side */
  .card--contact .brand-name { position: absolute; left: 60px; top: 48px; }
  .card--contact .wordmark { font-size: 46px; color: var(--brand-blue); }
  .card--contact .tagline { font-size: 10px; color: var(--brand-green); }
  .contact-block {
    position: absolute; left: 60px; top: 138px;
    color: var(--text-grey); font-size: 17px; line-height: 1.45;
  }
  .person-name {
    font-weight: 700; font-size: 22px; color: var(--brand-blue-deep);
    letter-spacing: 1px; line-height: 1.2;
  }
  .person-role { color: var(--brand-green); font-weight: 600; font-size: 17px; margin-bottom: 4px; }
  .contact-line { display: flex; align-items: center; gap: 10px; }
  .contact-line svg { width: 16px; height: 16px; fill: var(--brand-blue); flex: none; }
  .highlight { color: var(--brand-blue-deep); font-weight: 700; }

  /* Brand side */
  .skyline-area {
    position: absolute; left: 120px; top: 70px; width: 440px; height: 390px;
    background: linear-gradient(180deg, rgba(255,255,255,0) 0%, rgba(255,255,255,0.16) 100%);
  }
  .brand-lockup {
    position: absolute; left: 100px; top: 110px;
    display: flex; align-items: flex-start; gap: 22px;
  }
  .brand-square {
    width: 54px; height: 54px; border: 4px solid var(--on-green); flex: none;
  }
  .card--brand .wordmark { font-size: 56px; color: var(--on-green); }
  .card--brand .tagline { font-size: 12px; color: var(--on-green); }
  .book-online {
    position: absolute; left: 100px; top: 262px;
    font-size: 21px; font-weight: 600; color: var(--on-green);
  }
</style>
</head>
<body>
<main class="canvas">

  <section class="card card--contact" aria-label="Business card, contact side">
    <div class="brand-name">
      <span class="wordmark">The Harrowfield Clinic</span>
      <span class="tagline">Private General Practice</span>
    </div>

    <div class="contact-block">
      <p class="person-name">ALAN WHITBY</p>
      <p class="person-role">CEO/Founder</p>
      <p>FitVanta</p>
      <p>19 Bramblecote Lane</p>
      <p>London, EC2Z 4QJ</p>
      <p class="contact-line">
        <svg viewBox="0 0 24 24" aria-hidden="true"><path d="M6.6 10.8a15.1 15.1 0 0 0 6.6 6.6l2.2-2.2a1 1 0 0 1 1-.25 11.4 11.4 0 0 0 3.6.57 1 1 0 0 1 1 1V20a1 1 0 0 1-1 1A17 17 0 0 1 3 4a1 1 0 0 1 1-1h3.5a1 1 0 0 1 1 1c0 1.25.2 2.45.57 3.57a1 1 0 0 1-.25 1z"/></svg>
        <span>020 7946 0381</span>
      </p>
      <p class="contact-line">
        <svg viewBox="0 0 24 24" aria-hidden="true"><path d="M2 5h20v14H2z M4 7v.5l8 5 8-5V7l-8 5z" fill-rule="evenodd"/></svg>
        <span>bookings@harrowfieldclinic.example</span>
      </p>
      <p class="highlight">Book online : www.harrowfieldclinic.example</p>
      <p class="highlight">Open: Mon-Fri (early &amp; late appointments)</p>
    </div>
  </section>

  <section class="card card--brand" aria-label="Business card, brand side">
    <div class="skyline-area" role="img" aria-label="Faint City of London skyline illustration"></div>
    <div class="brand-lockup">
      <span class="brand-square" aria-hidden="true"></span>
      <div class="brand-name">
        <span class="wordmark">The Harrowfield Clinic</span>
        <span class="tagline">Private General Practice</span>
      </div>
    </div>
    <p class="book-online">Book online : www.harrowfieldclinic.example</p>
  </section>

</main>
</body>
</html>
```